Business Card Design Project

Recently had a new logo made up for my company and new business cards done as well. I have attached the logos for your viewing. Additional projects may be needed. Good luck!

Industry/Entity Type

Business

```html
<!DOCTYPE html>
<html lang="en">
<head>
<meta charset="utf-8">
<title>Harwell Financial Group – Business Card</title>
<link href="https://fonts.googleapis.com/css2?family=Cinzel:wght@400&family=Didact+Gothic&display=swap" rel="stylesheet">
<style>
  :root {
    --gold: #c9b17a;
    --ink: #1f1f22;
    --ink-soft: #2e2e32;
    --mark-fill: #121116;
    --card-top: #a3a3a6;
    --card-mid: #5f5f63;
    --card-bottom: #1b1a21;
    --card-light-top: #e6e6e8;
    --card-light-mid: #a9a9ad;
  }
  * { margin: 0; padding: 0; box-sizing: border-box; }
  html, body { width: 1200px; height: 848px; overflow: hidden; }
  body {
    position: relative;
    background: linear-gradient(105deg, #000 0%, #3a3a3a 18%, #9a9a9a 38%, #ffffff 58%, #f2f2f2 72%, #c2c2c2 88%, #9c9c9c 100%);
    font-family: "Didact Gothic", "Century Gothic", sans-serif;
  }
  .card {
    position: absolute;
    width: 648px;
    overflow: hidden;
    box-shadow: 0 0 0 1px rgba(0,0,0,0.35);
  }
  .card--back {
    left: 506px; top: 47px; height: 361px;
    background: linear-gradient(180deg, var(--card-top) 0%, var(--card-mid) 45%, var(--card-bottom) 100%);
  }
  .card--front {
    left: 44px; top: 463px; height: 347px;
    background: linear-gradient(180deg, var(--card-light-top) 0%, var(--card-light-mid) 48%, var(--card-mid) 70%, var(--card-bottom) 100%);
  }
  .gold-rule {
    position: absolute;
    left: 37px; right: 37px;
    height: 4px;
    background: var(--gold);
  }
  .brand {
    position: absolute;
    left: 0; right: 0;
    display: flex;
    align-items: center;
    justify-content: center;
    gap: 20px;
  }
  .brand__mark {
    width: 88px; height: 88px;
    border: 4px solid var(--gold);
    background: var(--mark-fill);
    flex: none;
  }
  .brand__name {
    font-family: "Cinzel", serif;
    font-weight: 400;
    font-size: 25px;
    letter-spacing: 1px;
    color: var(--gold);
    white-space: nowrap;
  }
  .website {
    position: absolute;
    left: 0; right: 0;
    text-align: center;
    font-size: 25px;
    line-height: 30px;
    color: var(--gold);
    letter-spacing: 0.5px;
  }
  .card--back .gold-rule--top { top: 105px; }
  .card--back .gold-rule--bottom { top: 267px; }
  .card--back .brand { top: 124px; }
  .card--back .website { top: 226px; }

  .contact {
    position: absolute;
    left: 34px; top: 24px;
    color: var(--ink);
  }
  .contact__name { font-size: 27px; color: var(--ink); line-height: 36px; }
  .contact__title { font-size: 19px; color: var(--ink-soft); line-height: 26px; }
  .contact__line {
    font-size: 19px; color: var(--ink-soft); line-height: 26px;
    display: flex; align-items: center; gap: 3px;
  }
  .contact__line--indent { padding-left: 20px; }
  .contact__phones { display: flex; gap: 120px; }
  .icon { width: 14px; height: 14px; flex: none; fill: var(--ink); }
  .card--front .gold-rule { top: 198px; }
  .card--front .brand { top: 216px; }
  .card--front .website { top: 302px; }
</style>
</head>
<body>
  <section class="card card--back" aria-label="Card back">
    <div class="gold-rule gold-rule--top"></div>
    <div class="brand">
      <div class="brand__mark"></div>
      <span class="brand__name">Harwell Financial Group</span>
    </div>
    <div class="website">www.harwellfinancial.com</div>
    <div class="gold-rule gold-rule--bottom"></div>
  </section>

  <section class="card card--front" aria-label="Card front">
    <div class="contact">
      <div class="contact__name">Daniel R. Harwell</div>
      <div class="contact__title">Estate Planning and Insurance Specialist</div>
      <div class="contact__line">
        <svg class="icon" viewBox="0 0 14 14"><rect x="1" y="1" width="12" height="13"/></svg>
        4200 Maple Crest Road, Suite 310E
      </div>
      <div class="contact__line contact__line--indent">Glenfield, New York 11850</div>
      <div class="contact__line">
        <svg class="icon" viewBox="0 0 14 14"><path d="M1 3h12v8H1z" fill="none" stroke="#1f1f22" stroke-width="1.4"/><path d="M1 3l6 5 6-5" fill="none" stroke="#1f1f22" stroke-width="1.4"/></svg>
        dharwell@harwellfinancial.com
      </div>
      <div class="contact__phones">
        <div class="contact__line">
          <svg class="icon" viewBox="0 0 14 14"><path d="M2 1l3 0 1 3-2 1.5c1 2 2.5 3.5 4.5 4.5L10 8l3 1v3c-6 1-12-5-11-11z"/></svg>
          516-555-0142
        </div>
        <div class="contact__line">
          <svg class="icon" viewBox="0 0 14 14"><rect x="3" y="0" width="9" height="14" rx="1.5"/></svg>
          516-555-0187
        </div>
      </div>
    </div>
    <div class="gold-rule"></div>
    <div class="brand">
      <div class="brand__mark"></div>
      <span class="brand__name">Harwell Financial Group</span>
    </div>
    <div class="website">www.harwellfinancial.com</div>
  </section>
</body>
</html>
```